Design a Professional Business Card for Velmora Arcs

Design a business card for Velmora Arcs, we are a National Sport Court Company.

West Region Address: 4175 Quill Harbor Ln, Suite #215 Englewood, Colorado 80467
East Region Address: 3817 Tamsin Rd E, Bradenton, Florida 34583

Target Market(s)

High End Residential & Institutional Clients

Industry/Entity Type

Design & Construction

Contact Information for Business Card

Logo/Brand/Colors/ name, number (provided in comments)

Requirements
Must have
• Colors only provided in logo
Should not have
• Any other colors not in existing logo (attached)

```html
<!DOCTYPE html>
<html lang="en">
<head>
<meta charset="utf-8">
<title>Velmora Arcs – Business Card</title>
<link href="https://fonts.googleapis.com/css2?family=Arimo:wght@400;700&display=swap" rel="stylesheet">
<style>
  :root {
    --navy: #1f3766;
    --green: #1d7a3c;
    --ink: #2b2b2b;
    --paper: #ffffff;
    --stage: #2a2a2a;
  }
  * { box-sizing: border-box; margin: 0; padding: 0; }
  html, body { width: 1200px; height: 977px; overflow: hidden; }
  body {
    background: var(--stage);
    font-family: "Arimo", Arial, sans-serif;
    position: relative;
  }
  .card {
    position: absolute;
    width: 560px;
    height: 340px;
    border-radius: 26px;
    overflow: hidden;
  }
  .card-back {
    left: 80px; top: 110px;
    background: var(--navy);
    display: flex; align-items: center; justify-content: center;
  }
  .card-front {
    left: 560px; top: 520px;
    background: var(--paper);
  }
  .brand { display: flex; align-items: center; gap: 16px; }
  .brand-mark { width: 86px; height: 86px; border-radius: 50%; background: var(--paper); }
  .brand-name {
    font-weight: 700; font-size: 44px; line-height: 1;
    letter-spacing: 2px; text-transform: uppercase; color: var(--paper);
  }
  .card-front .brand { position: absolute; right: 26px; top: 30px; gap: 12px; }
  .card-front .brand-mark { width: 54px; height: 54px; background: var(--navy); }
  .card-front .brand-name { font-size: 28px; color: var(--navy); letter-spacing: 1.5px; }

  .name-band {
    position: absolute; left: 0; top: 112px;
    width: 300px; height: 64px;
    background: var(--navy);
    padding: 10px 0 0 32px;
    color: var(--paper);
  }
  .name-band .person { font-weight: 700; font-size: 21px; }
  .name-band .role { font-size: 14px; margin-top: 4px; }

  .contacts {
    position: absolute; left: 32px; top: 212px;
    list-style: none; font-size: 13px; color: var(--ink);
  }
  .contacts li { display: flex; align-items: center; gap: 9px; margin-bottom: 7px; }
  .contacts svg { width: 12px; height: 12px; fill: var(--green); flex: none; }

  .address { position: absolute; top: 200px; font-size: 13px; line-height: 1.45; color: var(--ink); }
  .address h3 { font-size: 13px; font-weight: 700; color: var(--green); margin-bottom: 2px; }
  .address-west { left: 250px; }
  .address-east { left: 418px; }
</style>
</head>
<body>
  <section class="card card-back">
    <div class="brand">
      <span class="brand-mark"></span>
      <span class="brand-name">Velmora Arcs</span>
    </div>
  </section>

  <section class="card card-front">
    <div class="brand">
      <span class="brand-mark"></span>
      <span class="brand-name">Velmora Arcs</span>
    </div>

    <div class="name-band">
      <p class="person">Dorian L. Hask, ASLA</p>
      <p class="role">CEO &amp; Founder</p>
    </div>

    <ul class="contacts">
      <li><svg viewBox="0 0 24 24"><path d="M6.6 10.8a15 15 0 0 0 6.6 6.6l2.2-2.2a1 1 0 0 1 1-.25 11.4 11.4 0 0 0 3.6.57 1 1 0 0 1 1 1V20a1 1 0 0 1-1 1A17 17 0 0 1 3 4a1 1 0 0 1 1-1h3.5a1 1 0 0 1 1 1c0 1.25.2 2.45.57 3.57a1 1 0 0 1-.25 1z"/></svg>(303) 555-0147 (Direct)</li>
      <li><svg viewBox="0 0 24 24"><path d="M6.6 10.8a15 15 0 0 0 6.6 6.6l2.2-2.2a1 1 0 0 1 1-.25 11.4 11.4 0 0 0 3.6.57 1 1 0 0 1 1 1V20a1 1 0 0 1-1 1A17 17 0 0 1 3 4a1 1 0 0 1 1-1h3.5a1 1 0 0 1 1 1c0 1.25.2 2.45.57 3.57a1 1 0 0 1-.25 1z"/></svg>1-800-555-0192 (Main)</li>
      <li><svg viewBox="0 0 24 24"><path d="M2 5h20v14H2zm2 2v.5l8 5 8-5V7l-8 5z"/></svg>dorian@velmoraarcs.com</li>
      <li><svg viewBox="0 0 24 24"><circle cx="12" cy="12" r="10"/></svg>velmoraarcs.com</li>
    </ul>

    <div class="address address-west">
      <h3>West Region Address:</h3>
      <p>4175 Quill Harbor Ln<br>Suite #215 Englewood<br>Colorado 80467</p>
    </div>
    <div class="address address-east">
      <h3>East Region Address:</h3>
      <p>3817 Tamsin Rd E<br>Bradenton<br>Florida 34583</p>
    </div>
  </section>
</body>
</html>
```